Fast-casual chicken restaurant Brisket Barn needs a catering menu design

We need a catering menu designed for Brisket Barn. We are looking to design a 24x36in landscape menu board for our new catering menu. The catering memo attached includes our catering menu and Brisket Barn branding. More information about our brand can be found at https://brisketbarn-eats.example/.

```html
<!DOCTYPE html>
<html lang="en">
<head>
<meta charset="utf-8">
<title>Brisket Barn – Catering Menu</title>
<link rel="stylesheet" href="https://fonts.googleapis.com/css2?family=Montserrat:ital,wght@0,500;0,700;0,800;0,900;1,500&display=swap">
<style>
  :root{
    --red:#d9352a;
    --yellow:#fdd12f;
    --ink:#111111;
    --paper:#f5f4f2;
    --bg:#ffffff;
    --wood-dark:#6b3a1f;
    --wood-mid:#a0582c;
    --sauce:#c9401e;
  }
  *{margin:0;padding:0;box-sizing:border-box}
  html,body{width:1200px;height:1000px;overflow:hidden;background:var(--bg)}
  body{font-family:"Montserrat",Arial,sans-serif;color:var(--ink);position:relative}
  .board{position:absolute;left:30px;top:115px;width:1135px;height:755px;background:var(--paper);overflow:hidden}
  .stripe-red{position:absolute;left:0;top:0;width:8px;height:100%;background:var(--red)}
  .stripe-yellow{position:absolute;left:8px;top:0;width:28px;height:100%;background:var(--yellow)}
  .food-photo{position:absolute;left:36px;top:0;width:314px;height:100%;
    background:radial-gradient(circle at 70% 45%,var(--sauce) 0 18%,transparent 40%),
               radial-gradient(circle at 30% 20%,#e7a04a 0 12%,transparent 30%),
               linear-gradient(160deg,var(--wood-mid),var(--wood-dark))}
  .abs{position:absolute}
  .title{left:418px;top:144px;font-size:39px;font-weight:800;color:var(--red);letter-spacing:0.5px;line-height:1;white-space:nowrap}
  .dots{left:815px;top:160px}
  .heading{font-size:17px;font-weight:900;text-transform:uppercase;position:relative;display:inline-block;line-height:24px;padding:0 4px;z-index:0}
  .heading::before{content:"";position:absolute;left:0;right:-4px;top:3px;bottom:2px;background:var(--yellow);border-radius:3px 8px 4px 9px;z-index:-1;transform:skewX(-6deg)}
  .col-label{font-size:13px;font-weight:700;color:var(--yellow);text-transform:uppercase;position:absolute;top:4px}
  .menu-list{position:absolute;font-size:13.5px;line-height:18.5px}
  .item{margin-bottom:18.5px}
  .item-row{display:grid;font-weight:700}
  .deals .item-row{grid-template-columns:1fr 48px 70px}
  .per-person .item-row{grid-template-columns:1fr 48px 95px}
  .carte .item-row{grid-template-columns:1fr 80px 95px}
  .carte .item{margin-bottom:4.7px}
  .qty{text-align:center}
  .price{text-align:right}
  .cal{font-style:italic;font-weight:500}
  .desc{font-weight:500}
  .flavor-list{position:absolute;list-style:none;font-size:13.5px;font-weight:700;line-height:23px}
  .flavor-list li{display:flex;align-items:center;gap:10px;white-space:nowrap}
  .swatch{width:15px;height:15px;border-radius:50%;border:2px solid #e3e0dc;flex:none}
  .inline-list{list-style:none;font-size:13.5px;font-weight:700;position:absolute}
  .inline-list li{display:flex;align-items:center;gap:9px;position:absolute;white-space:nowrap}
</style>
</head>
<body>
<div class="board">
  <div class="stripe-red"></div>
  <div class="stripe-yellow"></div>
  <div class="food-photo" role="img" aria-label="Overhead photo of platters of fried chicken wings, tenders, waffle fries, onion rings and ribs on a wooden table"></div>
</div>

<h1 class="abs title">CATERING MENU</h1>
<svg class="abs dots" width="310" height="14" viewBox="0 0 310 14" aria-hidden="true">
  <g fill="#111">
    <circle cx="7" cy="7" r="6.5"/><circle cx="34" cy="7" r="6.5"/><circle cx="61" cy="7" r="6.5"/><circle cx="88" cy="7" r="6.5"/><circle cx="115" cy="7" r="6.5"/><circle cx="142" cy="7" r="6.5"/><circle cx="169" cy="7" r="6.5"/><circle cx="196" cy="7" r="6.5"/><circle cx="223" cy="7" r="6.5"/><circle cx="250" cy="7" r="6.5"/><circle cx="277" cy="7" r="6.5"/><circle cx="302" cy="7" r="6.5"/>
  </g>
</svg>

<div class="abs" style="left:418px;top:204px;width:335px;height:24px">
  <h2 class="heading">Packaged Deals</h2>
  <span class="col-label" style="left:210px">Feeds</span>
  <span class="col-label" style="right:0">Price</span>
</div>
<div class="menu-list deals" style="left:420px;top:232px;width:333px">
  <div class="item"><div class="item-row"><span>Family</span><span class="qty">4</span><span class="price">$24.99</span></div><div class="cal">(400-1000 CAL)</div><div class="desc">12 tenders, sauces, dressing, large side, 2L</div></div>
  <div class="item"><div class="item-row"><span>Tailgate</span><span class="qty">10</span><span class="price">$75.99</span></div><div class="cal">(400-1000 CAL)</div><div class="desc">20 tenders, 30 wings, sauces, 1 party side</div></div>
  <div class="item"><div class="item-row"><span>House Party</span><span class="qty">10</span><span class="price">$155.99</span></div><div class="cal">(400-1000 CAL)</div><div class="desc">20 tenders, 60 wings, 2 party sides,<br>2 party salads, dressings, 2 2L</div></div>
</div>

<div class="abs" style="left:788px;top:203px;width:334px;height:24px">
  <h2 class="heading">Per Person</h2>
  <span class="col-label" style="left:194px">Feeds</span>
  <span class="col-label" style="right:0">Price</span>
</div>
<div class="menu-list per-person" style="left:790px;top:231px;width:332px">
  <div class="item"><div class="item-row"><span>Snack</span><span class="qty">1</span><span class="price">$7.00</span></div><div class="cal">(400-1000 CAL)</div><div class="desc">2 tenders, sauce, dressing, 1 reg side</div></div>
  <div class="item"><div class="item-row"><span>Party</span><span class="qty">1</span><span class="price">$11.00</span></div><div class="cal">(400-1000 CAL)</div><div class="desc">2 tenders, 3 wings, sauce, dressing,<br>1 reg side, 12 oz/fountain drink</div></div>
  <div class="item"><div class="item-row"><span>Feast</span><span class="qty">1</span><span class="price">$15.00</span></div><div class="cal">(400-1000 CAL)</div><div class="desc">2 tenders, 6 wings, sauce, dressing,<br>1 reg side, dessert, 20 oz drink</div></div>
</div>

<div class="abs" style="left:418px;top:488px;width:335px;height:24px">
  <h2 class="heading">A La Carte</h2>
  <span class="col-label" style="left:157px">Increments</span>
  <span class="col-label" style="right:0">Price</span>
</div>
<div class="menu-list carte" style="left:420px;top:516px;width:333px">
  <div class="item"><div class="item-row"><span>Wings</span><span class="qty" style="white-space:nowrap">50 | 75 | 100</span><span class="price">$00.00</span></div><div class="cal">(400-1000 CAL)</div></div>
  <div class="item"><div class="item-row"><span>Tenders</span><span class="qty" style="white-space:nowrap">30 | 45 | 60</span><span class="price">$00.00</span></div><div class="cal">(400-1000 CAL)</div></div>
  <div class="item"><div class="item-row"><span>Waffle Fries</span><span class="qty">Party Size</span><span class="price">$13.99</span></div><div class="cal">(400-1000 CAL)</div></div>
  <div class="item"><div class="item-row"><span>Garlic Parm Tots</span><span class="qty">Party Size</span><span class="price">$13.99</span></div><div class="cal">(400-1000 CAL)</div></div>
  <div class="item"><div class="item-row"><span style="white-space:nowrap">Chicken Caesar Salad</span><span class="qty">Party Size</span><span class="price">$38.99</span></div><div class="cal">(400-1000 CAL)</div></div>
  <div class="item"><div class="item-row"><span>Caesar Salad</span><span class="qty">Party Size</span><span class="price">$27.99</span></div><div class="cal">(400-1000 CAL)</div></div>
  <div class="item"><div class="item-row"><span>Any Sauce</span><span class="qty">8 oz</span><span class="price">$1.99</span></div><div class="cal">(400-1000 CAL)</div></div>
  <div class="item"><div class="item-row"><span>Cheese Sauce</span><span class="qty">8 oz</span><span class="price">$2.49</span></div><div class="cal">(400-1000 CAL)</div></div>
</div>

<h2 class="heading abs" style="left:788px;top:488px;position:absolute">Flavors</h2>
<ul class="flavor-list" style="left:794px;top:514px">
  <li><span class="swatch" style="background:#e2c46a"></span>Honey Mustard</li>
  <li><span class="swatch" style="background:#a6231a"></span>Hot Lemon Pepper</li>
  <li><span class="swatch" style="background:#5a2014"></span>Jamaican Jerk</li>
  <li><span class="swatch" style="background:#9a2a18"></span>Mango Habanero</li>
  <li><span class="swatch" style="background:#b2301f"></span>Sweet Chilli</li>
</ul>

<h2 class="heading abs" style="left:968px;top:488px;position:absolute">Dry Rubs</h2>
<ul class="flavor-list" style="left:974px;top:514px">
  <li><span class="swatch" style="background:#b04a1c"></span>7 Pepper</li>
  <li><span class="swatch" style="background:#9c3418"></span>Cajun</li>
  <li><span class="swatch" style="background:#c9a24a"></span>Garlic Parm</li>
  <li><span class="swatch" style="background:#d0aa3c"></span>Lemon Pepper</li>
  <li><span class="swatch" style="background:#b85a28"></span>West Texas Mesquite</li>
</ul>

<h2 class="heading abs" style="left:788px;top:641px;position:absolute">BBQ</h2>
<ul class="flavor-list" style="left:794px;top:666px">
  <li><span class="swatch" style="background:#6a1e12"></span>Cajun BBQ</li>
  <li><span class="swatch" style="background:#4a1a10"></span>Citrus Chipotle</li>
  <li><span class="swatch" style="background:#3e1a10"></span>Golden BBQ</li>
  <li><span class="swatch" style="background:#4a1810"></span>Honey BBQ</li>
  <li><span class="swatch" style="background:#7a2012"></span>Kickin BBQ</li>
</ul>

<h2 class="heading abs" style="left:968px;top:641px;position:absolute">Buffalo</h2>
<ul class="flavor-list" style="left:974px;top:666px">
  <li><span class="swatch" style="background:#7a1a12"></span>Mild Mannered</li>
  <li><span class="swatch" style="background:#6a1410"></span>Smokehouse Heat</li>
  <li><span class="swatch" style="background:#70160f"></span>Red Ember</li>
  <li><span class="swatch" style="background:#5e120c"></span>Barn Burner</li>
  <li><span class="swatch" style="background:#66140e"></span>Firestorm</li>
</ul>

<h2 class="heading abs" style="left:786px;top:792px;position:absolute">Teriyaki</h2>
<ul class="inline-list" style="left:0;top:819px">
  <li style="left:791px"><span class="swatch" style="background:#3a1a10"></span>Cajun</li>
  <li style="left:908px"><span class="swatch" style="background:#4a1a12"></span>Spicy</li>
  <li style="left:1009px"><span class="swatch" style="background:#2e140c"></span>Traditional</li>
</ul>
</body>
</html>
```